Business Card Design for Loft Pictures

Hi we need a business card designed for a new aerial photography business we have started, we use UAV Drones to take photos for corporate, events, real estate, local government etc , the business name is Loft Pictures Australia, we have a facebook page that might help you come up with some designs - https://www.facebook.com/loftpicturesaustralia

We need to have and editable AI file so that we can use different names and contact details. details for one of the cards as follow:

Ned Harrow
phone: 03 5521 4736
Mobile: 0431 957 284
email: ned@loftpicturez.example
web: www.loftpictures.example

have now changed: Designer Payment:Committed

Target Market(s)

We are a Aerial Photography business using Drones and UAV

Industry/Entity Type

Business

Logo Text

Loft Pictures Australia

Requirements
Must have
• Colors to match logo and be part of Loft Pictures Brand

```html
<!DOCTYPE html>
<html lang="en">
<head>
<meta charset="utf-8">
<title>Loft Pictures Australia – Business Card</title>
<link rel="stylesheet" href="https://fonts.googleapis.com/css2?family=Great+Vibes&family=Montserrat:wght@400;600&display=swap">
<style>
  :root {
    --backdrop: #a9b2b0;
    --card-front: #ffffff;
    --card-back-top: #50605f;
    --card-back-bottom: #2c3737;
    --ink-dark: #2b2f31;
    --ink-light: #e9eeee;
    --script-mint: #cfeee6;
    --edge: #d9dddd;
  }
  * { box-sizing: border-box; margin: 0; padding: 0; }
  html, body { width: 1200px; height: 873px; overflow: hidden; }
  body {
    background: var(--backdrop);
    font-family: "Montserrat", sans-serif;
    position: relative;
  }
  .card {
    position: absolute;
    top: 293px;
    width: 500px;
    height: 286px;
    border-radius: 18px;
  }
  .card-front {
    left: 80px;
    background: var(--card-front);
    border: 2px solid var(--edge);
    display: flex;
    align-items: center;
    justify-content: center;
  }
  .brand-name {
    font-weight: 600;
    white-space: nowrap;
  }
  .card-front .brand-name {
    color: var(--ink-dark);
    font-size: 30px;
  }
  .card-back {
    left: 620px;
    background: linear-gradient(160deg, var(--card-back-top), var(--card-back-bottom));
    color: var(--ink-light);
  }
  .card-back .brand-name {
    position: absolute;
    top: 24px;
    right: 28px;
    font-size: 18px;
    color: var(--ink-light);
  }
  .holder-name {
    position: absolute;
    left: 26px;
    top: 124px;
    font-family: "Great Vibes", cursive;
    font-size: 50px;
    line-height: 1.2;
    color: var(--script-mint);
    font-weight: 400;
    white-space: nowrap;
  }
  .contact-list {
    list-style: none;
    position: absolute;
    font-size: 12px;
    font-weight: 400;
    letter-spacing: 0.3px;
  }
  .contact-list li {
    display: flex;
    align-items: center;
    gap: 10px;
    height: 26px;
    white-space: nowrap;
  }
  .contact-list svg { width: 15px; height: 15px; flex: none; }
  .contact-phones { left: 30px; top: 200px; }
  .contact-online { left: 278px; top: 96px; }
</style>
</head>
<body>
  <section class="card card-front" aria-label="Card front">
    <p class="brand-name">Loft Pictures Australia</p>
  </section>

  <section class="card card-back" aria-label="Card back">
    <p class="brand-name">Loft Pictures Australia</p>

    <ul class="contact-list contact-online">
      <li>
        <svg viewBox="0 0 16 16" aria-hidden="true"><rect x="1" y="3" width="14" height="10" rx="1" fill="none" stroke="currentColor" stroke-width="1.4"/><path d="M1.5 3.5 8 9l6.5-5.5" fill="none" stroke="currentColor" stroke-width="1.4"/></svg>
        ned@loftpicturez.example
      </li>
      <li>
        <svg viewBox="0 0 16 16" aria-hidden="true"><circle cx="8" cy="8" r="6.5" fill="none" stroke="currentColor" stroke-width="1.3"/><ellipse cx="8" cy="8" rx="2.8" ry="6.5" fill="none" stroke="currentColor" stroke-width="1.1"/><path d="M1.5 8h13M2.5 5h11M2.5 11h11" stroke="currentColor" stroke-width="1"/></svg>
        www.loftpictures.example
      </li>
    </ul>

    <h1 class="holder-name">Ned Harrow</h1>

    <ul class="contact-list contact-phones">
      <li>
        <svg viewBox="0 0 16 16" aria-hidden="true"><rect x="2" y="5" width="12" height="9" rx="1.5" fill="none" stroke="currentColor" stroke-width="1.4"/><path d="M3 5V3h10v2" fill="none" stroke="currentColor" stroke-width="1.4"/><circle cx="8" cy="9.5" r="2" fill="currentColor"/></svg>
        03 5521 4736
      </li>
      <li>
        <svg viewBox="0 0 16 16" aria-hidden="true"><rect x="4" y="1" width="8" height="14" rx="1.5" fill="none" stroke="currentColor" stroke-width="1.4"/><circle cx="8" cy="12.5" r="0.9" fill="currentColor"/></svg>
        0431 957 284
      </li>
    </ul>
  </section>
</body>
</html>
```